Etikett für Weißwein aus Deutschland - Lindenbrunn Müller-Thurgau
Zielgruppe
Wir sind eine Weinfirma und handeln mit handwerklich hergestellten, hochwertigen Weinen. Unsere Zielgruppe sind Weinliebhaber, die Wert auf Qualität, Authentizität und Personalisierung des Produktes und des Herstellers legen.
Aufgabenstellung
Der Name des Weins ist Lindenbrunn Müller-Thurgau. Er kommt vom RebenGilde Hasselbrück - siehe Kapsel von der Flasche. (alle rechtlichen Angaben werden auf dem Rückenetikett von der Kellerei gedruckt)
Das Hauptaugenmerk sollte auf der Rebsorte liegen, dafür habe ich ein antiques Bild von einer Rebe mitgeschickt - es können auch andere grafische Mittel verwendet werden - und als Hintergrundinformation einen langen Text zur Rebsorte Müller-Thurgau. Es ist ein Schoppenwein, d.h. ein Wein für den unkomplizierten Genuss unter Freunden.
Das Etikett sollte anzeigen, dass es sich um eine handwerklich hergestelltes Produkt handelt.

```html
<!DOCTYPE html>
<html lang="de">
<head>
<meta charset="utf-8">
<title>Lindenbrunn Müller-Thurgau – Etikett</title>
<link rel="stylesheet" href="https://fonts.googleapis.com/css2?family=Italiana&family=Pinyon+Script&display=swap">
<style>
  :root {
    --label-green: #84e022;
    --label-glow: #f4f9ec;
    --label-mid: #bde98a;
    --band-brown: #a3825c;
    --name-brown: #a88459;
    --script-white: #ffffff;
    --page: #ffffff;
    --engraving-dark: rgba(30, 30, 20, 0.55);
  }
  html, body {
    margin: 0;
    padding: 0;
    width: 1050px;
    height: 1200px;
    overflow: hidden;
    background: var(--page);
  }
  .wine-label {
    position: relative;
    width: 1050px;
    height: 1200px;
    border-radius: 40px;
    overflow: hidden;
    background: radial-gradient(ellipse 58% 55% at 50% 52%,
      var(--label-glow) 0%, var(--label-mid) 55%, var(--label-green) 100%);
  }
  .label-artwork {
    position: absolute;
    inset: 0;
    width: 1050px;
    height: 1200px;
  }
  .estate-name {
    font-family: "Italiana", serif;
    fill: var(--name-brown);
  }
  .variety-band {
    fill: var(--band-brown);
  }
  .variety-name {
    font-family: "Pinyon Script", cursive;
    fill: var(--script-white);
  }
</style>
</head>
<body>
  <main class="wine-label">
    <svg class="label-artwork" viewBox="0 0 1050 1200" xmlns="http://www.w3.org/2000/svg">
      <defs>
        <radialGradient id="insect-tone" cx="50%" cy="50%" r="50%">
          <stop offset="0%" stop-color="rgba(30,30,20,0.55)"/>
          <stop offset="70%" stop-color="rgba(30,30,20,0.25)"/>
          <stop offset="100%" stop-color="rgba(30,30,20,0)"/>
        </radialGradient>
        <radialGradient id="wing-tone" cx="50%" cy="50%" r="50%">
          <stop offset="0%" stop-color="rgba(60,60,40,0.22)"/>
          <stop offset="100%" stop-color="rgba(60,60,40,0)"/>
        </radialGradient>
      </defs>

      <g class="engraving" role="img" aria-label="Antiker Kupferstich einer Maulwurfsgrille mit ausgebreiteten Flügeln, schwarz auf grün">
        <ellipse cx="525" cy="600" rx="490" ry="200" fill="url(#wing-tone)"/>
        <ellipse cx="525" cy="610" rx="150" ry="520" fill="url(#insect-tone)"/>
      </g>

      <text class="estate-name" x="525" y="548" text-anchor="middle"
            font-size="190" textLength="720" lengthAdjust="spacingAndGlyphs">lindenbrunn</text>

      <rect class="variety-band" x="34" y="555" width="1016" height="145"/>

      <text class="variety-name" x="540" y="678" text-anchor="middle"
            font-size="150" textLength="985" lengthAdjust="spacingAndGlyphs">Müller Thurgau</text>
    </svg>
  </main>
</body>
</html>
```